Oxford Choir needs a concert poster!

22nd November is St Wendelin's Day, the Patron Saint of music. 100 years ago on that day, Rupert Calloway was born, famously dubbed the "greatest English composer since Marlowe". 50 years ago that day, three of the most prominent men in history died: this trifecta included theologian and author of 'Quelmor' R. P. Dunmore, philosopher and author of 'Silent Amber Shore' Peregrine Vostell, and one of America's most beloved presidents, Walter P. Hargrove.

In memory of these prominent figures of the 20th century, the Choir of St Oswin by the Tanner Row (the Parish Kirk of Fenwold) perform some of the world's best vocal music composed or inspired by these men. The playlist includes Calloway's 'Canticle for St Wendelin', G. F. Olbrich's 'Sieh, Vater, sieh', 'The Orchard' by Peregrine Vostell set to music by Percy Madden, and Clement Yardley' 'Hold her, sea, in quiet keeping', written specially for the memorial service of President Walter P Hargrove in Marlbury Grand Minster.

We are looking for a dramatic concert poster / or series of posters that encapsulate all these important aspects on this one day. Tickets will be set up on passgrabber.example - space for their logo will be needed.

22nd November 2013, 8pm
Radley Hall Oratory, Oxford
Choir of St Oswin by the Tanner Row
Giles Pemberton-Roe
Tickets: £5

Mostly students and staff from the Universities of Oxford and Whitfield, but also singers from local Oxfordshire choral societies who have a passion for singing and the repertoire. Local musical professionals and appreciators. Not really suitable for children. Cultured adults that support local artistic projects and go to live classical concerts. Higher-end readership. I would like to charge much more for the ticket prices (in order to reflect the quality of the performance) but Oxford is haemorrhaging quality concerts for very little, and the competition is fierce. This poster needs to stand out from the crowd of other events going on, and perhaps be coupled with an inventive marketing strategy.

• St Oswin by the Tanner Row logo
Passgrabber.example logo

My name prominently displayed

```html
<!DOCTYPE html>
<html lang="en">
<head>
<meta charset="utf-8">
<title>Choir of St Oswin by the Tanner Row – Concert Poster</title>
<link rel="stylesheet" href="https://fonts.googleapis.com/css2?family=Cinzel:wght@400;600;700&display=swap">
<style>
  :root {
    --ink: #5a5a5a;
    --ink-dark: #444;
    --paper: #ececec;
    --paper-light: #f7f7f7;
    --rule: #8c8c8c;
    --teal: #1f6f7a;
    --teal-deep: #0f3f4c;
    --green: #2fbf7a;
    --blue: #2a5fa8;
    --violet: #5a2a9a;
    --badge-top: #6a6a6a;
    --badge-bottom: #2e2e2e;
    --white: #ffffff;
  }
  * { box-sizing: border-box; margin: 0; padding: 0; }
  html, body { width: 849px; height: 1200px; overflow: hidden; background: var(--white); }
  .poster {
    position: relative; width: 849px; height: 1200px; overflow: hidden;
    background: linear-gradient(180deg, var(--paper-light) 0%, var(--paper) 60%, #e2e2e2 100%);
    font-family: "Cinzel", serif; color: var(--ink); text-align: center;
  }
  .hero-art, .bottom-band, .ornament { position: absolute; left: 0; width: 849px; display: block; }
  .hero-art { top: 0; height: 400px; }
  .ornament { height: 44px; }
  .ornament-top { top: 428px; }
  .ornament-bottom { top: 1016px; }
  .bottom-band { top: 1060px; height: 80px; }

  .event-date, .event-venue {
    position: absolute; left: 0; width: 100%;
    font-size: 38px; font-weight: 400; letter-spacing: 1px; color: var(--ink);
  }
  .event-date { top: 494px; }
  .event-venue { top: 538px; font-size: 34px; }
  .rule { position: absolute; height: 2px; background: var(--rule); }
  .rule-venue { top: 588px; left: 250px; width: 350px; height: 1px; }
  .rule-name-top { top: 910px; left: 0; width: 849px; height: 1px; }
  .rule-name-bottom { top: 982px; left: 0; width: 849px; height: 1px; }

  .choir-name { position: absolute; top: 618px; left: 0; width: 100%; color: var(--ink); }
  .choir-name .main { display: block; font-size: 56px; font-weight: 700; line-height: 1.05; }
  .choir-name .sub { display: block; font-size: 26px; font-weight: 700; letter-spacing: 1px; }

  .programme {
    position: absolute; top: 740px; left: 40px; width: 769px;
    font-size: 19px; font-weight: 700; line-height: 1.4; color: var(--ink);
  }
  .tickets {
    position: absolute; top: 848px; right: 0; width: 235px; height: 42px;
    background: linear-gradient(180deg, var(--badge-top), var(--badge-bottom));
    color: var(--white); font-size: 27px; font-weight: 700; line-height: 42px; text-align: center;
    border-radius: 6px 0 0 6px;
  }
  .conductor {
    position: absolute; top: 918px; left: 0; width: 100%;
    font-size: 42px; font-weight: 400; color: var(--ink);
  }
  .footer {
    position: absolute; top: 1140px; left: 0; width: 849px; height: 60px; background: var(--white);
    display: flex; align-items: center; justify-content: center; gap: 50px;
  }
  .partner { display: flex; align-items: center; gap: 8px; font-size: 17px; font-weight: 700; color: var(--ink-dark); }
  .partner .mark { width: 14px; height: 14px; background: var(--blue); }
</style>
</head>
<body>
<main class="poster">
  <svg class="hero-art" viewBox="0 0 849 400" role="img" aria-label="Photograph of a conductor in a suit raising his baton over sheet music, washed in teal, green and blue light">
    <defs>
      <linearGradient id="heroWash" x1="0" y1="0" x2="1" y2="1">
        <stop offset="0" stop-color="#0d3a4a"/>
        <stop offset="0.45" stop-color="#1f6f7a"/>
        <stop offset="1" stop-color="#2fbf7a"/>
      </linearGradient>
      <linearGradient id="edgeWash" x1="0" y1="0" x2="1" y2="0">
        <stop offset="0" stop-color="#2a5fa8" stop-opacity="0.8"/>
        <stop offset="0.1" stop-color="#2a5fa8" stop-opacity="0"/>
        <stop offset="0.9" stop-color="#2fbf7a" stop-opacity="0"/>
        <stop offset="1" stop-color="#2fbf7a" stop-opacity="0.9"/>
      </linearGradient>
    </defs>
    <polygon points="0,0 849,0 849,395 0,300" fill="url(#heroWash)"/>
    <polygon points="0,0 849,0 849,395 0,300" fill="url(#edgeWash)"/>
  </svg>

  <svg class="ornament ornament-top" viewBox="0 0 849 44" role="img" aria-label="Row of grey flourish scrollwork ornaments">
    <rect x="0" y="8" width="849" height="28" fill="#b8b8b8" opacity="0.55"/>
  </svg>

  <p class="event-date">22nd November 2013, 8pm</p>
  <p class="event-venue">Radley Hall Oratory, Oxford</p>
  <div class="rule rule-venue"></div>

  <h1 class="choir-name">
    <span class="main">Choir of St Oswin</span>
    <span class="sub">by the Tanner Row</span>
  </h1>

  <p class="programme">Calloway's 'Canticle for St Wendelin', G. F. Olbrich's 'Sieh, Vater, sieh', 'The Orchard' by Peregrine Vostell set to music by Percy Madden, Clement Yardley' 'Hold her, sea, in quiet keeping' and more!</p>

  <div class="tickets">Tickets: £5</div>

  <div class="rule rule-name-top"></div>
  <p class="conductor">Giles Pemberton-Roe</p>
  <div class="rule rule-name-bottom"></div>

  <svg class="ornament ornament-bottom" viewBox="0 0 849 44" role="img" aria-label="Row of grey flourish scrollwork ornaments">
    <rect x="0" y="8" width="849" height="28" fill="#b8b8b8" opacity="0.55"/>
  </svg>

  <svg class="bottom-band" viewBox="0 0 849 80" aria-hidden="true">
    <defs>
      <linearGradient id="bandWash" x1="0" y1="0" x2="1" y2="0">
        <stop offset="0" stop-color="#5a2a9a"/>
        <stop offset="0.6" stop-color="#2a5fa8"/>
        <stop offset="1" stop-color="#1f6f7a"/>
      </linearGradient>
    </defs>
    <polygon points="0,20 849,0 849,80 0,80" fill="url(#bandWash)"/>
  </svg>

  <footer class="footer">
    <div class="partner"><span class="mark"></span>St Oswin by the Tanner Row</div>
    <div class="partner">Passgrabber.example</div>
  </footer>
</main>
</body>
</html>
```